Health Coaching Flyer for New Clients

I need a two-sided flyer (3.5" x 8.5" preferred or 5" x 7") to distribute to potential coaching clients. My business name is Talvora Health & Wellness Coaching. My business is focused on helping people with habit changes that contribute to their overall well-being. I would like the design colors to be gender neutral. I would like a small photo of myself near the "my name is Jen" statement. Please feel free to change the logo color to match the design.

Target Market(s)

Adults of all ages.

Font styles to use
Serif

Requirements
Must have
• Emphasize my opening question (found in health coaching brochure - attached).
• Small picture of myself near "my name is Jen" statement.
Should not have
• No light of pastel colors.

```html
<!DOCTYPE html>
<html lang="en">
<head>
<meta charset="utf-8">
<title>Talvora Health &amp; Wellness Coaching – Flyer</title>
<link href="https://fonts.googleapis.com/css2?family=Josefin+Sans:wght@300;400&family=Caveat:wght@500&family=Patrick+Hand&display=swap" rel="stylesheet">
<style>
  :root{
    --bg:#d9dadb;
    --charcoal:#3b3b3b;
    --ink:#151515;
    --white:#ffffff;
    --steel-a:#c9d2d8;
    --steel-b:#8e9aa3;
    --sky-a:#3fb4e4;
    --sky-b:#1d8fc7;
    --lime:#c9dc3c;
    --grey-a:#9b9b9b;
    --grey-b:#5e5e5e;
  }
  *{box-sizing:border-box;margin:0;padding:0}
  html,body{width:1200px;height:802px;overflow:hidden}
  body{background:var(--bg);position:relative;font-family:"Josefin Sans",sans-serif;color:var(--white)}
  .panel{position:absolute;top:16px;width:320px;height:770px;background:var(--charcoal);overflow:hidden;box-shadow:0 6px 18px rgba(0,0,0,.25)}
  .front{left:250px}
  .back{left:630px}

  .brand-bar{background:var(--ink);height:96px;display:flex;align-items:center;padding:0 24px}
  .brand-name{font-family:"Josefin Sans",sans-serif;font-weight:400;font-size:19px;line-height:1.25;color:var(--white)}

  .hero-photo{position:absolute;left:0;top:96px;width:320px;height:280px;
    background:linear-gradient(135deg,var(--steel-a),var(--steel-b))}
  .question{position:absolute;right:14px;top:110px;width:150px;text-align:center;
    font-family:"Caveat",cursive;font-size:30px;line-height:1.12;color:#333}
  .portrait{position:absolute;left:80px;top:336px;width:160px;height:160px;border-radius:50%;
    border:3px solid var(--white);background:linear-gradient(160deg,var(--grey-a),var(--grey-b))}
  .intro-name{position:absolute;left:0;width:100%;top:512px;text-align:center;font-weight:400;font-size:25px}
  .intro-text{position:absolute;left:28px;right:28px;top:552px;text-align:center;font-weight:300;font-size:12.6px;line-height:1.55}

  .coach-title{font-family:"Patrick Hand",cursive;font-weight:400;font-size:27px;padding:26px 20px 10px}
  .traits{list-style:none;padding:0 18px 0 20px}
  .traits li{display:flex;gap:10px;font-family:"Patrick Hand",cursive;font-size:14px;line-height:1.2;margin-bottom:11px}
  .traits svg{flex:none;width:20px;height:20px;margin-top:1px}
  .invite{position:absolute;left:0;top:372px;width:320px;height:210px;
    background:linear-gradient(135deg,var(--lime) 0%,var(--sky-a) 35%,var(--sky-b) 100%)}
  .invite-text{position:absolute;left:22px;right:22px;top:432px;text-align:center;
    font-family:"Caveat",cursive;font-size:15px;line-height:1.2;color:var(--ink)}
  .invite-text p+p{margin-top:12px}
  .contact-call{position:absolute;right:20px;top:596px;text-align:right;font-family:"Patrick Hand",cursive;font-size:17px;line-height:1.2}
  .contact-card{position:absolute;left:0;top:664px;width:320px;height:62px;background:var(--white);color:var(--ink);padding:6px 18px 0}
  .contact-name{font-weight:400;font-size:30px;letter-spacing:1px;line-height:1}
  .contact-lines{font-size:12.5px;margin-top:5px}
  .back-brand{position:absolute;left:18px;right:18px;top:726px;height:44px;display:flex;align-items:center}
  .back-brand .brand-name{font-size:16px}
</style>
</head>
<body>

<section class="panel front">
  <header class="brand-bar">
    <span class="brand-name">Talvora Health &amp; Wellness Coaching</span>
  </header>
  <div class="hero-photo" role="img" aria-label="Photo of a stethoscope around a heart-shaped bowl of fruit, nuts and grains on a wooden table"></div>
  <p class="question">Need<br>support in<br>making real,<br>lasting<br>lifestyle<br>and behavior<br>changes?</p>
  <div class="portrait" role="img" aria-label="Round portrait photo of Jen"></div>
  <h2 class="intro-name">My Name Is Jen.</h2>
  <p class="intro-text">I am studying to become a THRIVE-Certified Functional Health Coach. My training involves many science-based practices that improve both our health and how we grow and change as humans. I now have the opportunity to turn that knowledge into practice by coaching actual clients interested in improving their own health and well-being.</p>
</section>

<section class="panel back">
  <h2 class="coach-title">Functional health coaches...</h2>
  <ul class="traits">
    <li><svg viewBox="0 0 20 20"><rect x="2" y="4" width="14" height="14" fill="none" stroke="#fff" stroke-width="1.6"/><path d="M5 10l4 4 9-11" fill="none" stroke="#fff" stroke-width="2"/></svg>Leverage your strengths rather than focus on your weaknesses</li>
    <li><svg viewBox="0 0 20 20"><rect x="2" y="4" width="14" height="14" fill="none" stroke="#fff" stroke-width="1.6"/><path d="M5 10l4 4 9-11" fill="none" stroke="#fff" stroke-width="2"/></svg>Support you in finding your own strategies and motivation for change</li>
    <li><svg viewBox="0 0 20 20"><rect x="2" y="4" width="14" height="14" fill="none" stroke="#fff" stroke-width="1.6"/><path d="M5 10l4 4 9-11" fill="none" stroke="#fff" stroke-width="2"/></svg>Provide a judgment-free zone and support your autonomy</li>
    <li><svg viewBox="0 0 20 20"><rect x="2" y="4" width="14" height="14" fill="none" stroke="#fff" stroke-width="1.6"/><path d="M5 10l4 4 9-11" fill="none" stroke="#fff" stroke-width="2"/></svg>Use an experimental mindset to find and develop sustainable habits</li>
    <li><svg viewBox="0 0 20 20"><rect x="2" y="4" width="14" height="14" fill="none" stroke="#fff" stroke-width="1.6"/><path d="M5 10l4 4 9-11" fill="none" stroke="#fff" stroke-width="2"/></svg>Act as your accountability partner as you reach your unique health goals; whether they be improving sleep, diet, fitness, social connection, or reducing stress.</li>
  </ul>
  <div class="invite" role="img" aria-label="Photo of a yoga mat, water bottle, sneakers and dumbbells on a blue floor"></div>
  <div class="invite-text">
    <p>I would like to invite you to participate with me as a client as I continue to hone my coaching skills. We can develop a plan and schedule that aligns with your goals.</p>
    <p>As a way to give back to my community, I am offering new clients six free coaching sessions. This is a limited time offer.</p>
  </div>
  <p class="contact-call">Please contact me.<br>I'm ready to support you as you<br>work to improve your health.</p>
  <div class="contact-card">
    <div class="contact-name">JEN TALVORA</div>
    <div class="contact-lines">Call: 555-018-2740 | talvorahwc@mailbox.com</div>
  </div>
  <div class="back-brand">
    <span class="brand-name">Talvora Health &amp; Wellness Coaching</span>
  </div>
</section>

</body>
</html>
```